prophetic Novel: Disastrous Varnholm games in Paris

Creation of a cover for a book in French: a humorous novel on the catastrophic organization of the 2024 Varnholm Games in Paris: heavy traffic, poor security, Enormous budget…
AUTHOR: Marc-Antoine Tulle
TITLE: Teacups at the Quarry
SUB-TITLE: Brellac 2024 Varnholms. Valmorel, wake up, they've gone crazy
PUBLISHER (AT THE BOTTOM OF THE COVER): Brisolle Editions

Industry/Entity Type

Book

Requirements
Must have
• comedy, drama

```html
<!DOCTYPE html>
<html lang="en">
<head>
<meta charset="utf-8">
<title>Teacups at the Quarry — Book Cover</title>
<link rel="stylesheet" href="https://fonts.googleapis.com/css2?family=Josefin+Sans:wght@400;600;700&family=Cormorant+SC:wght@500;600&display=swap">
<style>
  :root {
    --page-bg: #e9e6e1;
    --storm-dark: #0c1418;
    --storm-teal: #2f6b62;
    --sky-glow: #8fa070;
    --ember: #c8542a;
    --facade-gold: #c9a646;
    --street-teal: #1d4a52;
    --taxi-yellow: #e0b63c;
    --bus-red: #b8321e;
    --ink-white: #ffffff;
    --ink-soft: #f1efe9;
  }
  * { margin: 0; padding: 0; box-sizing: border-box; }
  html, body {
    width: 1200px;
    height: 1200px;
    overflow: hidden;
    background: var(--page-bg);
  }
  .canvas {
    position: relative;
    width: 1200px;
    height: 1200px;
  }
  .book-cover {
    position: absolute;
    left: 246px;
    top: 47px;
    width: 736px;
    height: 1076px;
    overflow: hidden;
    background: var(--storm-dark);
  }
  .cover-scene {
    position: absolute;
    inset: 0;
    background:
      radial-gradient(ellipse 40% 18% at 92% 3%, var(--ember) 0%, transparent 70%),
      radial-gradient(ellipse 55% 22% at 55% 12%, var(--storm-teal) 0%, transparent 75%),
      radial-gradient(ellipse 30% 14% at 52% 40%, var(--sky-glow) 0%, transparent 80%),
      radial-gradient(ellipse 22% 40% at 8% 42%, var(--facade-gold) 0%, transparent 75%),
      radial-gradient(ellipse 30% 24% at 82% 68%, var(--bus-red) 0%, transparent 75%),
      radial-gradient(ellipse 30% 20% at 62% 80%, var(--taxi-yellow) 0%, transparent 75%),
      radial-gradient(ellipse 45% 45% at 45% 70%, var(--street-teal) 0%, transparent 80%),
      linear-gradient(180deg, #10181b 0%, #1b2a28 35%, #14262a 60%, #0a0f12 100%);
  }
  .cover-scene::after {
    content: "";
    position: absolute;
    inset: 0;
    background: linear-gradient(180deg, rgba(0,0,0,0.25) 0%, transparent 30%, transparent 75%, rgba(0,0,0,0.55) 100%);
  }
  .title {
    position: absolute;
    left: 91px;
    top: 108px;
    font-family: "Josefin Sans", sans-serif;
    font-weight: 600;
    color: var(--ink-white);
    letter-spacing: 5px;
    line-height: 1;
    text-transform: uppercase;
  }
  .title-line { display: block; white-space: nowrap; }
  .title-big { font-size: 78px; }
  .title-line--second { margin-top: 2px; }
  .title-small { font-size: 42px; letter-spacing: 3px; margin-right: 12px; }
  .subtitle {
    position: absolute;
    left: 91px;
    top: 270px;
    font-family: "Cormorant SC", serif;
    font-weight: 600;
    font-size: 27px;
    letter-spacing: 2.5px;
    line-height: 39px;
    color: var(--ink-soft);
    text-transform: lowercase;
    white-space: nowrap;
  }
  .subtitle-year { font-size: 33px; }
  .author {
    position: absolute;
    left: 0;
    right: 0;
    top: 980px;
    text-align: center;
    font-family: "Josefin Sans", sans-serif;
    font-weight: 600;
    font-size: 39px;
    letter-spacing: 4px;
    line-height: 1;
    color: var(--ink-white);
    text-transform: uppercase;
  }
  .publisher {
    position: absolute;
    left: 0;
    right: 0;
    top: 1040px;
    text-align: center;
    font-family: "Josefin Sans", sans-serif;
    font-weight: 400;
    font-size: 22px;
    letter-spacing: 4px;
    line-height: 1;
    color: var(--ink-soft);
    text-transform: uppercase;
  }
</style>
</head>
<body>
  <main class="canvas">
    <section class="book-cover">
      <div class="cover-scene" role="img" aria-label="Stormy sky over a city boulevard jammed with cars, yellow taxis and red buses between tall stone buildings"></div>

      <h1 class="title">
        <span class="title-line title-big">Teacups</span>
        <span class="title-line title-line--second"><span class="title-small">at the</span><span class="title-big">Quarry</span></span>
      </h1>

      <p class="subtitle">
        brellac <span class="subtitle-year">2024</span> varnholms<br>
        valmorel, wake up, they've gone crazy
      </p>

      <p class="author">Marc-Antoine Tulle</p>
      <p class="publisher">Brisolle Editions</p>
    </section>
  </main>
</body>
</html>
```